Project Halcyon PowerPoint Design

This is a PPT design for Power & Utilities company who are in the process of a technology upgrade for their Finance department. We are looking to develop a branded PPT for Project Halcyon (specifically HALCYON). Why does Halcyon resonate? "The Earth is pointed almost directly at Halcyon. During the course of the night,
Halcyon does not rise or set, but remains in nearly the same spot above the
northern horizon year- round while the other stars circle around it."
Halcyon represents the guiding principles that manage, monitor and
control the organizations financials.

Target Market(s)

Finance stakeholders impacted by technology enhancement

Font styles to use
Serif
Other font styles liked:
• Arial

Colors
0054AA
0677BA
7BADD7
CADEEF
E8F1F8

Requirements
Must have
• Various slide layout ( Cover slide, content slide, divider, etc). Attached is the logo and corporate colors
Nice to have
• Over the top creativity

```html
<!DOCTYPE html>
<html lang="en">
<head>
<meta charset="utf-8">
<title>Project Halcyon – Presentation Slides</title>
<link href="https://fonts.googleapis.com/css2?family=Arimo:wght@400;700&family=Roboto:wght@300;400&display=swap" rel="stylesheet">
<style>
  :root{
    --stage:#333133;
    --white:#ffffff;
    --brand:#2a4c9e;
    --brand-deep:#1e4a9a;
    --ink:#111111;
    --text:#222222;
    --panel:#eceff6;
    --chart-bg:#f4f1f2;
    --bar-teal:#147c8c;
    --bar-navy:#0b2540;
    --cover-a:#0d3a8c;
    --cover-b:#3f72c2;
    --photo-a:#cfd4dc;
    --photo-b:#5d6470;
    --ring-purple:#5a2fd8;
    --ring-teal:#16b3a2;
    --ring-red:#ec2f45;
  }
  *{margin:0;padding:0;box-sizing:border-box}
  html,body{width:1200px;height:3288px;overflow:hidden}
  body{background:var(--stage);font-family:"Arimo",Arial,sans-serif;color:var(--text);position:relative}

  .slide{position:absolute;left:102px;width:1002px;height:564px;background:var(--white);overflow:hidden}
  .slide--cover{top:128px}
  .slide--photo-list{top:737px}
  .slide--two-col{top:1346px}
  .slide--chart{top:1954px}
  .slide--process{top:2563px}

  /* brand wordmark */
  .brand{position:absolute;display:flex;flex-direction:column;align-items:flex-end;color:var(--brand);font-family:"Arimo",Arial,sans-serif;font-weight:400;line-height:1}
  .brand__kicker{font-size:13px;letter-spacing:4px;margin-bottom:2px}
  .brand__name{font-size:33px;letter-spacing:3px}
  .brand--light{color:var(--white)}
  .brand--cover .brand__kicker{font-size:25px;letter-spacing:7px;margin-bottom:4px}
  .brand--cover .brand__name{font-size:60px;letter-spacing:6px}

  /* cover */
  .cover-photo{position:absolute;inset:0;background:linear-gradient(135deg,var(--cover-b) 0%,#2f5fb0 45%,var(--cover-a) 100%)}
  .slide--cover .brand{left:50%;top:218px;transform:translateX(-50%)}

  /* bullet lists */
  .bullets{list-style:none}
  .bullets li{position:relative;padding-left:17px;font-size:14.5px;line-height:31.3px;color:var(--text)}
  .bullets li::before{content:"";position:absolute;left:0;top:11px;border-left:5px solid var(--brand-deep);border-top:4.5px solid transparent;border-bottom:4.5px solid transparent}

  /* slide 2 */
  .side-photo{position:absolute;left:0;top:0;width:511px;height:564px;background:linear-gradient(160deg,var(--photo-a) 0%,#9aa1ab 50%,var(--photo-b) 100%)}
  .slide--photo-list .brand{left:568px;top:36px}
  .slide--photo-list .slide__title{position:absolute;left:570px;top:106px;width:330px;font-size:20px;font-weight:700;line-height:29px;color:var(--ink)}
  .slide--photo-list .bullets{position:absolute;left:570px;top:177px}

  /* slide 3 */
  .slide--two-col .brand{left:28px;top:28px}
  .panel{position:absolute;top:102px;width:466px;height:435px;background:var(--panel);padding:36px 34px 0}
  .panel--left{left:18px}
  .panel--right{left:507px}
  .panel__title{font-size:16.5px;font-weight:700;color:var(--brand-deep);letter-spacing:.2px;margin-bottom:14px}
  .panel .bullets li{line-height:30.3px}

  /* slide 4 */
  .slide--chart .brand{left:31px;top:26px}
  .slide--chart .slide__title{position:absolute;left:26px;top:108px;font-family:"Roboto",Arial,sans-serif;font-weight:400;font-size:26px;line-height:36px;color:var(--ink)}
  .bar-chart{position:absolute;left:0;top:0}
  .chart-notes{position:absolute;left:563px;top:214px;width:395px;font-size:13px;line-height:22px;color:var(--text)}
  .chart-notes p{margin-bottom:22px}

  /* slide 5 */
  .slide--process .brand{left:31px;top:26px}
  .slide--process .slide__title{position:absolute;left:0;right:0;top:84px;text-align:center;font-size:18px;font-weight:700;color:var(--ink)}
  .slide--process .slide__lead{position:absolute;left:178px;width:600px;top:130px;text-align:center;font-size:13.4px;line-height:19px;color:var(--text)}
  .process-rings{position:absolute;left:0;top:0}
  .step{position:absolute;top:355px;width:184px;text-align:center}
  .step__title{font-size:13px;font-weight:700;color:var(--ink);margin-bottom:12px}
  .step__text{font-size:9.8px;line-height:13.4px;color:var(--text)}
  .step--one{left:121px}
  .step--two{left:393px}
  .step--three{left:680px}
</style>
</head>
<body>

<section class="slide slide--cover">
  <div class="cover-photo" role="img" aria-label="Business team reviewing financial charts on tablets and laptops, blue toned"></div>
  <div class="brand brand--cover brand--light"><span class="brand__kicker">PROJECT</span><span class="brand__name">HALCYON</span></div>
</section>

<section class="slide slide--photo-list">
  <div class="side-photo" role="img" aria-label="Hands holding a clipboard with printed financial charts and a pen"></div>
  <div class="brand"><span class="brand__kicker">PROJECT</span><span class="brand__name">HALCYON</span></div>
  <h2 class="slide__title">Lorem Ipsum is simply dummy text of the printing</h2>
  <ul class="bullets">
    <li>Contrary to popular belief, Lorem Ipsum</li>
    <li>There are many variations of passages of L</li>
    <li>It is a long established fact that a reader will be</li>
    <li>These cases are perfectly simple</li>
    <li>it will frequently occur that pleasures have</li>
    <li>Nam libero tempore, cum soluta nobis est</li>
    <li>To take a trivial example, which of us ever</li>
    <li>Excepteur sint occaecat cupidatat non proident</li>
    <li>sunt in culpa qui officia deserunt mollit</li>
    <li>The generated Lorem Ipsum</li>
    <li>Various versions have evolved over the years</li>
  </ul>
</section>

<section class="slide slide--two-col">
  <div class="brand"><span class="brand__kicker">PROJECT</span><span class="brand__name">HALCYON</span></div>
  <div class="panel panel--left">
    <h3 class="panel__title">LOREM IPSUM IS SIMPLY DUMMY</h3>
    <ul class="bullets">
      <li>Contrary to popular belief, Lorem Ipsum</li>
      <li>There are many variations of passages of L</li>
      <li>It is a long established fact that a reader will be</li>
      <li>These cases are perfectly simple</li>
      <li>it will frequently occur that pleasures have</li>
      <li>Nam libero tempore, cum soluta nobis est</li>
      <li>To take a trivial example, which of us ever</li>
      <li>Excepteur sint occaecat cupidatat non proident</li>
      <li>sunt in culpa qui officia deserunt mollit</li>
      <li>The generated Lorem Ipsum</li>
      <li>Various versions have evolved over the years</li>
    </ul>
  </div>
  <div class="panel panel--right">
    <h3 class="panel__title">LOREM IPSUM IS SIMPLY DUMMY</h3>
    <ul class="bullets">
      <li>Many desktop publishing packages</li>
      <li>Lorem Ipsum as their default model text, and a search</li>
      <li>Various versions have evolved over the years</li>
      <li>sometimes by accident, sometimes on purpose</li>
      <li>It has survived not only five</li>
      <li>Many desktop publishing packages and web page</li>
      <li>It is a long established fact that a reader</li>
      <li>Lorem Ipsum as their default model text, and a search</li>
      <li>Various versions have evolved over the years</li>
      <li>sometimes by accident, sometimes on purpose</li>
      <li>Lorem Ipsum as their default model text, and a search</li>
    </ul>
  </div>
</section>

<section class="slide slide--chart">
  <div class="brand"><span class="brand__kicker">PROJECT</span><span class="brand__name">HALCYON</span></div>
  <h2 class="slide__title">Lorem Ipsum is simply dummy text of<br>the printing and typesetting</h2>
  <svg class="bar-chart" width="560" height="540" viewBox="0 0 560 540" font-family="Arimo, Arial, sans-serif">
    <rect x="52" y="216" width="478" height="274" fill="var(--chart-bg)"/>
    <g font-size="9" fill="#333" text-anchor="end">
      <text x="44" y="219">800</text><text x="44" y="253">700</text><text x="44" y="287">600</text>
      <text x="44" y="322">500</text><text x="44" y="356">400</text><text x="44" y="390">300</text>
      <text x="44" y="424">200</text><text x="44" y="459">100</text><text x="44" y="493">0</text>
    </g>
    <g>
      <rect x="54" y="455.7" width="25" height="34.3" fill="var(--bar-teal)"/>
      <rect x="87.8" y="440.3" width="25" height="49.7" fill="var(--bar-navy)"/>
      <rect x="121.6" y="428.3" width="25" height="61.7" fill="var(--bar-teal)"/>
      <rect x="155.4" y="414.6" width="25" height="75.4" fill="var(--bar-navy)"/>
      <rect x="189.2" y="375.3" width="25" height="114.7" fill="var(--bar-teal)"/>
      <rect x="223" y="339.3" width="25" height="150.7" fill="var(--bar-navy)"/>
      <rect x="256.8" y="262.2" width="25" height="227.8" fill="var(--bar-navy)"/>
      <rect x="290.6" y="339.3" width="25" height="150.7" fill="var(--bar-teal)"/>
      <rect x="324.4" y="349.6" width="25" height="140.4" fill="var(--bar-navy)"/>
      <rect x="358.2" y="366.7" width="25" height="123.3" fill="var(--bar-teal)"/>
      <rect x="392" y="385.5" width="25" height="104.5" fill="var(--bar-navy)"/>
      <rect x="425.8" y="356.4" width="25" height="133.6" fill="var(--bar-teal)"/>
      <rect x="459.6" y="409.5" width="25" height="80.5" fill="var(--bar-navy)"/>
      <rect x="493.4" y="433.5" width="25" height="56.5" fill="var(--bar-teal)"/>
    </g>
    <g font-size="6.6" fill="#333" text-anchor="middle">
      <text x="66.5" y="506">151,161</text><text x="100.3" y="506">161,171</text><text x="134.1" y="506">171,181</text>
      <text x="167.9" y="506">181,191</text><text x="201.7" y="506">191,201</text><text x="235.5" y="506">201,211</text>
      <text x="269.3" y="506">211,221</text><text x="303.1" y="506">221,231</text><text x="336.9" y="506">231,241</text>
      <text x="370.7" y="506">241,251</text><text x="404.5" y="506">251,261</text><text x="438.3" y="506">261,271</text>
      <text x="472.1" y="506">271,281</text><text x="505.9" y="506">281,291</text>
    </g>
  </svg>
  <div class="chart-notes">
    <p>Contrary to popular belief, Lorem Ipsum is not simply random text. It has roots in a piece of classical Latin literature from 45 BC, making it over 2000 years old. Daniel Whitcombe, a Latin professor at Ashford College</p>
    <p>There are many variations of passages of Lorem Ipsum available, but the majority have suffered alteration in some form, by injected humour, or randomised words which don't look even slightly believable.</p>
    <p>Lorem Ipsum is simply dummy text of the printing and typesetting industry. Lorem Ipsum has been the industry's standard.</p>
  </div>
</section>

<section class="slide slide--process">
  <div class="brand"><span class="brand__kicker">PROJECT</span><span class="brand__name">HALCYON</span></div>
  <h2 class="slide__title">Lorem Ipsum is simply dummy text of the printing</h2>
  <p class="slide__lead">There are many variations of passages of Lorem Ipsum available, but the majority have suffered alteration in some form, by injected humour, or randomised words which don't look even slightly believable. If you are going to use a passage of Lorem Ipsum, you need to be sure there isn't anything embarrassing hidden in the middle of text.</p>
  <svg class="process-rings" width="1002" height="564" viewBox="0 0 1002 564">
    <defs>
      <linearGradient id="ring-purple" x1="0" y1="0" x2="1" y2="1">
        <stop offset="0" stop-color="#7a45e6"/><stop offset="1" stop-color="var(--ring-purple)"/>
      </linearGradient>
      <linearGradient id="link-purple-teal" gradientUnits="userSpaceOnUse" x1="300" y1="0" x2="400" y2="0">
        <stop offset="0" stop-color="var(--ring-purple)"/><stop offset="1" stop-color="var(--ring-teal)"/>
      </linearGradient>
      <linearGradient id="link-teal-red" gradientUnits="userSpaceOnUse" x1="575" y1="0" x2="690" y2="0">
        <stop offset="0" stop-color="var(--ring-teal)"/><stop offset="1" stop-color="var(--ring-red)"/>
      </linearGradient>
      <linearGradient id="ring-red" gradientUnits="userSpaceOnUse" x1="680" y1="300" x2="700" y2="470">
        <stop offset="0" stop-color="var(--ring-red)"/><stop offset="1" stop-color="#a3283d"/>
      </linearGradient>
    </defs>
    <g fill="none" stroke-width="4" stroke-linecap="round">
      <circle cx="213" cy="383" r="120" fill="#fff" stroke="#f1f1f4" stroke-width="10"/>
      <circle cx="485" cy="383" r="120" fill="#fff" stroke="#f1f1f4" stroke-width="10"/>
      <circle cx="772" cy="383" r="120" fill="#fff" stroke="#f1f1f4" stroke-width="10"/>
      <path d="M293 288 A124 124 0 1 0 308 463" stroke="url(#ring-purple)"/>
      <path d="M308 463 C350 420 350 330 390 303" stroke="url(#link-purple-teal)"/>
      <path d="M390 303 A124 124 0 0 1 594 325" stroke="var(--ring-teal)"/>
      <path d="M378 426 A124 124 0 0 0 580 463" stroke="var(--ring-teal)"/>
      <path d="M580 463 C625 420 630 330 677 303" stroke="url(#link-teal-red)"/>
      <path d="M677 303 A124 124 0 1 1 692 470" stroke="url(#ring-red)"/>
    </g>
    <circle cx="297" cy="283" r="7.5" fill="var(--ring-purple)"/>
    <circle cx="608" cy="318" r="7.5" fill="var(--ring-teal)"/>
    <circle cx="378" cy="426" r="7.5" fill="var(--ring-teal)"/>
    <circle cx="692" cy="470" r="7.5" fill="#9a2a3e"/>
    <g fill="none" stroke="#3a3a3a" stroke-width="3" stroke-linejoin="round">
      <path d="M213 286 l18 6 v12 c0 12 -8 19 -18 24 c-10 -5 -18 -12 -18 -24 v-12 z"/>
      <path d="M205 306 l6 6 l10 -11" stroke-linecap="round"/>
    </g>
    <g fill="#3a3a3a">
      <rect x="462" y="296" width="7" height="16" rx="1"/>
      <rect x="501" y="296" width="7" height="16" rx="1"/>
      <path d="M470 299 l10 -4 l8 4 l12 -2 v12 l-10 8 l-4 -3 l-4 3 l-4 -3 l-8 -3 z"/>
      <path d="M484 300 l-7 6 l3 3 l8 -5 z" fill="#fff"/>
    </g>
    <g fill="#3a3a3a">
      <rect x="756" y="310" width="6" height="10"/>
      <rect x="765" y="303" width="6" height="17"/>
      <rect x="774" y="296" width="6" height="24"/>
      <rect x="783" y="289" width="6" height="31"/>
      <path d="M755 305 l16 -13 l6 4 l10 -9" fill="none" stroke="#3a3a3a" stroke-width="2"/>
    </g>
  </svg>
  <div class="step step--one">
    <div class="step__title">LOREM IPSUM</div>
    <p class="step__text">There are many variations of passages of Lorem Ipsum available, but the majority have suffered alteration in some form, by injected humour, or randomised words which don't look even slightly</p>
  </div>
  <div class="step step--two">
    <div class="step__title">LOREM IPSUM</div>
    <p class="step__text">There are many variations of passages of Lorem Ipsum available, but the majority have suffered alteration in some form, by injected humour, or randomised words which don't look even slightly</p>
  </div>
  <div class="step step--three">
    <div class="step__title">LOREM IPSUM</div>
    <p class="step__text">There are many variations of passages of Lorem Ipsum available, but the majority have suffered alteration in some form, by injected humour, or randomised words which don't look even slightly</p>
  </div>
</section>

</body>
</html>
```